Web design for boutique law firm

Web design for law firm; practice areas include:
-international intellectual property counseling
-general corporate (contract negotiation, licensing, distribution agreements
-see my *very* outdated website at www.pvtlegalhouse.com: here is some of the home page content:

"PVT Law Group enjoys providing proactive, business-minded, efficient legal solutions for individuals and companies that benefit from major law firm experience at reasonable rates.

Some areas of emphasis include:

Counseling individuals and companies with respect to clearing, selecting, securing, managing, commercializing, and protecting intellectual property assets around the world. This includes traditional global brand management, marketing, advertising, and enforcement work as well as litigation.
PVT Law Group also provides general counseling services for individuals and businesses, from start-up advice to sophisticated business transactions strategy, agreement negotiating, dispute resolution, and litigation.
Before founding PVT Law Group in 2008, Curtis L. Abernathy led the Trademark, Copyright, & Brand Management Group for Falkner & Ingleby's Seattle office. Curtis was also a senior associate at Silicon Valley based Hartwell, Bexley, Oduya, & Penrose."

Target Market(s)

Clients/potential clients needing tier one, international intellectual property advice with "mega" law firm experience for much less than what we were/would be charging at the "mega firms".

Industry/Entity Type

Legal

Number of Pages Required

4 page

Font styles to use
Serif
Sans Serif

Colors

Designer to choose colors to be used in the design.

Requirements
Must have
• +Improvement over everything on current site at www.pvtlegalhouse.com.
• +Pictures/bios for me and my team (four of us right now).
• +Easy to update and add/remove content.
• +Must be superior in design (look, feel, ease of use, classy and elegant, but hip, reflects international practice).
• +i have logos and color schemes (see current website) but will consider improvements.
Nice to have
• Let me know your thoughts.
Should not have
• No cheese; no overt sales pitches or marketing (since law firm).

```html
<!DOCTYPE html>
<html lang="en">
<head>
<meta charset="utf-8">
<title>PVT Law Group PLLC</title>
<link rel="stylesheet" href="https://fonts.googleapis.com/css2?family=Questrial&family=Didact+Gothic&display=swap">
<style>
:root{
  --accent:#f28a30;
  --ink:#2b2b2b;
  --muted:#555;
  --line:#d9d9d9;
  --paper:#fff;
  --footer:#1c1c1c;
  --hero-dark:#5a4a3e;
  --hero-light:#d8cdb8;
}
*{margin:0;padding:0;box-sizing:border-box}
html,body{width:1200px;height:2233px;overflow:hidden;background:var(--paper)}
body{position:relative;font-family:"Didact Gothic",sans-serif;color:var(--ink)}
.abs{position:absolute}

/* header */
.brand{left:54px;top:132px;font-family:"Questrial",sans-serif;font-size:38px;letter-spacing:2px;color:var(--muted);white-space:nowrap}
.brand-rule{left:54px;top:194px;width:449px;height:2px;background:var(--accent)}
.social{left:886px;top:44px;width:275px;height:66px;border-radius:33px;background:linear-gradient(#f4f4f4,#e2e2e2)}
.social span{position:absolute;top:31px;width:26px;height:26px;border-radius:50%;background:#6b6b6b}
.nav{top:164px;font-family:"Questrial",sans-serif;font-size:21px;letter-spacing:1px;color:var(--ink)}
.nav.active{color:var(--accent)}
.nav-underline{left:643px;top:196px;width:75px;height:1px;background:var(--muted)}
.search{left:871px;top:228px;width:272px;height:31px;border:1px solid var(--line);box-shadow:inset 0 1px 3px rgba(0,0,0,.12)}
.search-label{left:8px;top:8px;font-size:10px;color:#aaa}
.search-btn{right:0;top:-1px;width:40px;height:31px;background:#333}

/* hero */
.hero{left:0;top:328px;width:1200px;height:752px;background:radial-gradient(ellipse at 45% 65%,var(--hero-light) 0%,#b9a993 40%,var(--hero-dark) 100%)}
.hero-mark{left:0;width:1200px;text-align:center;color:#f2f2f2;font-family:"Questrial",sans-serif}
.hero-mark.big{top:145px;font-size:44px;letter-spacing:4px}
.hero-mark.small{top:214px;font-size:15px;letter-spacing:1px}
.hero-title{left:0;top:340px;width:1200px;text-align:center;font-family:"Questrial",sans-serif;font-size:33px;color:#fff;text-shadow:0 2px 4px rgba(0,0,0,.45)}
.hero-tag{left:0;top:399px;width:1200px;text-align:center;font-size:15px;color:#222;word-spacing:4px}
.hero-cta{left:509px;top:565px;width:179px;height:38px;background:var(--accent);color:#fff;font-family:"Questrial",sans-serif;font-size:21px;text-align:center;line-height:38px;border:1px solid #fff}

/* team */
.team-heading{left:0;top:1185px;width:1200px;text-align:center;font-family:"Questrial",sans-serif;font-size:20px;letter-spacing:.5px}
.portrait{left:107px;top:1297px;width:143px;height:181px;background:linear-gradient(#9a9a9a,#5c5c5c);border:1px solid #888}
.member-name{left:60px;top:1480px;width:237px;text-align:center;font-size:17px}
.bio-btn{left:122px;top:1528px;width:109px;height:24px;background:var(--accent);color:#fff;font-size:14px;text-align:center;line-height:24px}
.team-copy{left:503px;top:1290px;width:661px;text-align:center;font-size:12px;line-height:16px;color:var(--muted)}
.team-copy p{margin-bottom:10px}
.team-copy p:last-child{margin-top:14px}
.team-copy .firm{color:var(--accent)}
.team-btn{left:734px;top:1505px;width:222px;height:45px;border:1px solid #333;font-size:14px;text-align:center;line-height:43px}

/* about */
.divider{left:0;top:1629px;width:1200px;height:1px;background:#444}
.col{top:1650px;width:522px;font-size:17px;line-height:23px;color:#333}
.col-left{left:64px;text-align:center}
.col-right{left:619px;text-align:justify;text-align-last:center}
.col p{margin-bottom:23px}
.col .firm{color:var(--accent)}
.col .sub{color:var(--accent);margin:10px 0 22px}
.col .item{text-align:justify;text-align-last:center;border-left:2px solid var(--accent);padding-left:4px;margin-bottom:0}

/* footer */
.foot-mark{left:550px;top:2072px;width:100px;height:100px;border-radius:50%;border:2px solid #999;text-align:center;line-height:96px;font-family:"Questrial",sans-serif;font-size:30px;color:#888}
.footer{left:0;top:2204px;width:1200px;height:29px;background:var(--footer);color:#ccc;font-size:12px;text-align:center;line-height:29px}
</style>
</head>
<body>
<header>
  <div class="abs brand">PVT LAW GROUP PLLC</div>
  <div class="abs brand-rule"></div>
  <div class="abs social" aria-label="Social links">
    <span style="left:53px"></span><span style="left:89px"></span><span style="left:125px"></span><span style="left:161px;background:#d9463b"></span><span style="left:197px"></span>
  </div>
  <nav>
    <div class="abs nav active" style="left:645px">HOME</div>
    <div class="abs nav-underline"></div>
    <div class="abs nav" style="left:745px">EXPERIENCE</div>
    <div class="abs nav" style="left:904px">ABOUT US</div>
    <div class="abs nav" style="left:1042px">CONTACT</div>
  </nav>
  <div class="abs search">
    <span class="abs search-label">Search</span>
    <div class="abs search-btn">
      <svg width="40" height="31" viewBox="0 0 40 31"><circle cx="18" cy="14" r="4.5" fill="none" stroke="#fff" stroke-width="2"/><line x1="21" y1="17" x2="25" y2="21" stroke="#fff" stroke-width="2.5"/></svg>
    </div>
  </div>
</header>

<section class="abs hero" role="img" aria-label="Photograph of a lawyer's hand signing a document with a pen at a desk">
  <div class="abs hero-mark big">PVT</div>
  <div class="abs hero-mark small">PVT GROUP</div>
  <h1 class="abs hero-title" style="font-weight:400">EXPERT LEGAL SOLUTIONS</h1>
  <div class="abs hero-tag">Imagine &nbsp;| Secure &nbsp;| Protect</div>
  <div class="abs hero-cta">GET STARTED</div>
</section>

<section>
  <h2 class="abs team-heading" style="font-weight:400">MEET THE TEAM</h2>
  <div class="abs portrait" role="img" aria-label="Portrait photo of Curtis L. Abernathy"></div>
  <div class="abs member-name">Curtis L. Abernathy</div>
  <div class="abs bio-btn">VIEW BIO</div>
  <div class="abs team-copy">
    <p><span class="firm">PVT Law Group</span> has teamed with Greta Solheim to provide clients with experienced docketing, paralegal, and intellectual property management and protection services.</p>
    <p>Greta has over 23 years experience in the legal profession with 13 of those years dedicated to trademark paralegal and docketing services. Greta is deeply experienced with the docketing system used by PVT Law Group.</p>
    <p>Curtis and Greta bring over 30 years of legal experience to the table, with no less than 20 years dedicated to intellectual property management, maintenance, and protection services.</p>
  </div>
  <div class="abs team-btn">MEET OUR TEAM</div>
</section>

<section>
  <div class="abs divider"></div>
  <div class="abs col col-left">
    <p style="margin-bottom:0"><span class="firm">PVT Law Group</span> enjoys providing proactive, business-minded, efficient legal solutions for individuals and companies that benefit from major law firm experience at reasonable rates.</p>
    <p class="sub">Some areas of emphasis include :</p>
    <p class="item">counseling individuals and companies with respect to clearing, selecting, securing, managing, commercializing, and protecting intellectual property assets around the world. This includes traditional global brand management, marketing, advertising, and enforcement work as well as litigation</p>
    <p class="item">PVT Law Group also provides general counseling services for individuals and businesses, from start-up advice to sophisticated business transactions strategy, agreement negotiating, dispute resolution, and litigation.</p>
  </div>
  <div class="abs col col-right">
    <p>Before founding PVT Law Group in 2008, Curtis L. Abernathy led the Trademark, Copyright, &amp; Brand Management Group for Falkner &amp; Ingleby's Seattle office. Curtis was also a senior associate at Silicon Valley based Hartwell, Bexley, Oduya, &amp; Penrose.</p>
    <p>Over the years, Curtis has worked with start-ups to Fortune 25 corporations spanning various industries and continues to team with legal professionals in the U.S. and abroad to best serve his clients' needs.</p>
    <p>For example, PVT Law Group recently successfully enforced a company's branding rights in Europe while obtaining an order of costs in the company's favor. Curtis is also working on trademark filing programs for companies using the Madrid Protocol as well as national applications in jurisdictions all over the world, including Africa, Canada, the European Union, and Mexico among others.</p>
  </div>
</section>

<footer>
  <div class="abs foot-mark">PVT</div>
  <div class="abs footer">| &copy;2008-2010 PVT LAW GROUP PLLC &nbsp;| &nbsp;All Rights Reserved &nbsp;| &nbsp;contact@pvtlegalhouse.com &nbsp;|</div>
</footer>
</body>
</html>
```